nutrition company business card

I would like to have a business card that has two sides, one being the green color from the Company name on the logo. I am open to ideas and looks that work with my logo. I like the idea of having a negative image of the tree on the green side.

For my information on the card I must have:
Linda Moorcombe
415-872-6041
lindamoorcombe@quellmail.net

This area will need to be updated once I complete my schooling.

Reason: I need to extend my deadline by one day as I have been sick the last week and not had time to review all the new designs. Thank you.

Industry/Entity Type

Nutrition

Requirements
Must have
• I would like to have a business card that has two sides, one being the green color from the Company name on the logo. I am open to ideas and looks that work with my logo. I like the idea of having a negative image of the tree on the green side.
• For my information on the card I must have:
• Linda Moorcombe
• 415-872-6041
• lindamoorcombe@quellmail.net
• This area will need to be updated once I complete my schooling.

```html
<!DOCTYPE html>
<html lang="en">
<head>
<meta charset="utf-8">
<title>Rooted Table – Business Card</title>
<link href="https://fonts.googleapis.com/css2?family=Quicksand:wght@400;500&family=Delius&display=swap" rel="stylesheet">
<style>
  :root {
    --canvas-bg: #ece7e1;
    --brand-green: #a9cb37;
    --card-white: #ffffff;
    --bark-brown: #8c7d76;
    --text-brown: #7f716b;
    --edge: rgba(0, 0, 0, 0.08);
  }
  * { margin: 0; padding: 0; box-sizing: border-box; }
  html, body {
    width: 1200px;
    height: 1000px;
    overflow: hidden;
    background: var(--canvas-bg);
  }
  .canvas {
    position: relative;
    width: 1200px;
    height: 1000px;
  }
  .card {
    position: absolute;
    left: 340px;
    width: 540px;
    height: 343px;
    box-shadow: 0 0 0 1px var(--edge);
  }
  .card--front {
    top: 131px;
    background: var(--brand-green);
    color: var(--card-white);
    text-align: center;
  }
  .front-mark {
    position: absolute;
    left: 50%;
    top: 89px;
    width: 104px;
    height: 104px;
    margin-left: -52px;
    border: 4px solid var(--card-white);
    border-radius: 50%;
  }
  .brand-name {
    position: absolute;
    left: 0;
    right: 0;
    top: 200px;
    font-family: "Quicksand", sans-serif;
    font-weight: 500;
    font-size: 29px;
    line-height: 34px;
    letter-spacing: 0.3px;
  }
  .brand-tagline {
    position: absolute;
    left: 0;
    right: 0;
    top: 234px;
    font-family: "Quicksand", sans-serif;
    font-weight: 500;
    font-size: 17px;
    line-height: 20px;
    letter-spacing: 1.3px;
  }
  .card--back {
    top: 526px;
    background: var(--card-white);
  }
  .back-mark {
    position: absolute;
    left: 76px;
    top: 110px;
    width: 122px;
    height: 122px;
    border: 5px solid var(--bark-brown);
    border-radius: 50%;
    display: flex;
    align-items: center;
    justify-content: center;
    text-align: center;
    font-family: "Quicksand", sans-serif;
    font-weight: 500;
    font-size: 17px;
    line-height: 20px;
    color: var(--bark-brown);
  }
  .contact-list {
    position: absolute;
    left: 242px;
    top: 130px;
    list-style: none;
    font-family: "Delius", sans-serif;
    color: var(--text-brown);
    font-size: 16px;
    letter-spacing: 0.6px;
  }
  .contact-item {
    display: flex;
    align-items: center;
    height: 26.5px;
  }
  .contact-item--name { font-size: 17.5px; }
  .contact-icon {
    width: 11px;
    height: 11px;
    margin-right: 7px;
    fill: var(--brand-green);
    flex: none;
  }
</style>
</head>
<body>
<main class="canvas">
  <section class="card card--front">
    <div class="front-mark"></div>
    <h1 class="brand-name">Rooted Table</h1>
    <p class="brand-tagline">simple food for busy homes</p>
  </section>

  <section class="card card--back">
    <div class="back-mark">Rooted<br>Table</div>
    <ul class="contact-list">
      <li class="contact-item contact-item--name">
        <svg class="contact-icon" viewBox="0 0 12 12" aria-hidden="true"><circle cx="6" cy="3.2" r="2.6"/><path d="M1 12c0-3.4 2.2-5.6 5-5.6s5 2.2 5 5.6z"/></svg>
        Linda Moorcombe
      </li>
      <li class="contact-item">
        <svg class="contact-icon" viewBox="0 0 12 12" aria-hidden="true"><path d="M2.4 0.6l2 2.2-1 1.6c.8 1.6 2 2.8 3.6 3.6l1.6-1 2.2 2-1.2 2.2C5 11 1 7 .4 1.8z"/></svg>
        415-872-6041
      </li>
      <li class="contact-item">
        <svg class="contact-icon" viewBox="0 0 12 12" aria-hidden="true"><path d="M0 2.5h12v1L6 7 0 3.5z"/><path d="M0 5l6 3.5L12 5v4.5H0z"/></svg>
        lindamoorcombe@quellmail.net
      </li>
    </ul>
  </section>
</main>
</body>
</html>
```